Promotion Layer (UI Design)

What we need is not a classical App Design.
We need a UI Design for a SDK, which appears as Layer in different apps.
The layer will contain a list/library which will show cool goodies for the app user.

The attached file will give you all the details you need to start.

Note: The Screenshots do show app content. But these are just place holders.
The content is NOT part of the design task. Because we just provide the layer...

The crucial part of this task is, to create a UI design, that is stylish, simple and does not harm the 3rd party app, where it will be showed. While you design it, allways try to think "do I like this, when it appears in my own app"

Your files should be made in the right size/dimensions of ios.

Industry/Entity Type

Library

Font styles to use
Sans Serif

Requirements
Must have
• Must fit the iOS 7 Style

```html
<!DOCTYPE html>
<html lang="de">
<head>
<meta charset="utf-8">
<title>Promotion Layer – Navigation States</title>
<link href="https://fonts.googleapis.com/css2?family=Roboto:wght@300;400;500&display=swap" rel="stylesheet">
<style>
  :root {
    --stage: #282828;
    --divider: #0c0c0c;
    --app-bg: #f4f1ef;
    --app-edge: #dcd8d5;
    --card: #ffffff;
    --card-text: #a9a9a9;
    --note-text: #b9b9b9;
    --tile-bg: #ffffff;
    --tile-alt: #ececef;
    --tile-border: #d9d9dc;
    --strip-bg: #f1f1f1;
    --strip-text: #7d7d7d;
    --icon-blue: #6eb0e2;
    --icon-yellow: #f8c66b;
    --icon-teal: #92d7c2;
    --icon-gray: #555555;
    --sky-top: #4f86c9;
    --sky-bottom: #dfe9f4;
    --sea-top: #1d2c78;
    --sea-bottom: #4b8fd8;
  }
  * { box-sizing: border-box; margin: 0; padding: 0; }
  html, body { width: 1200px; height: 2466px; overflow: hidden; background: var(--stage); }
  body { font-family: 'Roboto', sans-serif; }

  .state { position: absolute; left: 0; width: 1200px; height: 818px; background: var(--stage); overflow: hidden; }
  .state--full   { top: 0; }
  .state--hidden { top: 824px; }
  .state--idle   { top: 1648px; }
  .divider { position: absolute; left: 0; width: 1200px; height: 6px; background: var(--divider); }

  .app-screen { position: absolute; left: 0; top: 0; width: 398px; height: 818px; background: var(--app-bg); overflow: hidden; }
  .app-screen::before { content: ""; position: absolute; left: 24px; top: 0; width: 2px; height: 100%; background: var(--app-edge); }
  .state--full .app-screen { border-top: 9px solid #fff; }

  .placeholder-photo { position: absolute; left: 94px; width: 304px; }
  .placeholder-photo--sky { top: 15px; height: 219px; background: linear-gradient(180deg, var(--sky-top), var(--sky-bottom) 70%, #8c8680); }
  .placeholder-photo--sea { top: 460px; height: 346px; background: linear-gradient(180deg, var(--sea-top), var(--sea-bottom) 75%, #e7eef8); }
  .content-card { position: absolute; left: 94px; top: 234px; width: 304px; height: 122px; background: var(--card); border-bottom: 2px solid #e4e1de; }
  .content-card__title { position: absolute; left: 36px; top: 38px; font-size: 38px; font-weight: 300; color: var(--card-text); white-space: nowrap; }

  .layer-clip { position: absolute; left: 26px; top: 109px; width: 372px; height: 522px; overflow: hidden; }
  .promo-tab { position: absolute; top: 0; left: 0; width: 256px; height: 522px; display: flex; box-shadow: 2px 0 6px rgba(0,0,0,.12); }
  .state--hidden .promo-tab { left: -105px; }

  .promo-tab__tiles { width: 174px; display: flex; flex-direction: column; }
  .promo-tile { width: 174px; height: 174px; background: var(--tile-bg); border: 2px solid var(--tile-border); display: flex; align-items: center; justify-content: center; }
  .promo-tile + .promo-tile { border-top: none; }
  .promo-tile--alt { background: var(--tile-alt); }
  .promo-tile svg { fill: none; stroke: currentColor; stroke-width: 4; stroke-linecap: round; stroke-linejoin: round; }
  .icon--ticket { color: var(--icon-blue); }
  .icon--like   { color: var(--icon-yellow); }
  .icon--device { color: var(--icon-teal); }
  .state--idle .promo-tile svg { color: var(--icon-gray); }
  .state--idle .promo-tile svg.icon--ticket { color: var(--icon-blue); }

  .promo-tab__label { width: 82px; height: 522px; background: var(--strip-bg); border: 2px solid var(--tile-border); border-left: none; position: relative; }
  .promo-tab__text { position: absolute; left: 14px; top: 18px; height: 420px; writing-mode: vertical-rl; transform: rotate(180deg); font-size: 41px; font-weight: 500; letter-spacing: 1px; color: var(--strip-text); text-align: left; line-height: 50px; }
  .promo-tab__arrow { position: absolute; left: 16px; bottom: 18px; width: 48px; height: 48px; fill: none; stroke: var(--strip-text); stroke-width: 5; stroke-linecap: round; stroke-linejoin: round; opacity: .8; }

  .state-note { position: absolute; font-size: 41px; font-weight: 300; color: var(--note-text); line-height: 54px; }
  .state--full .state-note   { left: 478px; top: 356px; }
  .state--hidden .state-note { left: 478px; top: 376px; }
  .state--idle .state-note   { left: 500px; top: 344px; }
</style>
</head>
<body>

<section class="state state--full">
  <div class="app-screen">
    <div class="placeholder-photo placeholder-photo--sky" role="img" aria-label="App content photo: stone statue against a blue sky"></div>
    <div class="content-card"><span class="content-card__title">Platzhalter</span></div>
    <div class="placeholder-photo placeholder-photo--sea" role="img" aria-label="App content photo: tropical fish leaping from a water bowl"></div>
    <div class="layer-clip">
      <nav class="promo-tab">
        <div class="promo-tab__tiles">
          <div class="promo-tile"><svg class="icon--ticket" width="44" height="128" viewBox="0 0 44 128"><path d="M8 3h28a5 5 0 0 1 5 5v117l-19-18-19 18V8a5 5 0 0 1 5-5z"/><circle cx="22" cy="32" r="8"/></svg></div>
          <div class="promo-tile"><svg class="icon--like" width="120" height="120" viewBox="0 0 80 80"><path d="M26 34 38 10c4-5 11-2 10 5l-3 14h21c6 0 9 5 7 10l-6 27c-1 4-4 7-8 7H26z"/><path d="M8 34h18v40H8z"/></svg></div>
          <div class="promo-tile promo-tile--alt"><svg class="icon--device" width="80" height="130" viewBox="0 0 48 80"><rect x="4" y="3" width="40" height="74" rx="6"/><path d="M4 14h40M4 64h40"/><circle cx="24" cy="71" r="1.5"/></svg></div>
        </div>
        <div class="promo-tab__label">
          <span class="promo-tab__text">NEUE ANGEBOTE</span>
          <svg class="promo-tab__arrow" viewBox="0 0 48 48"><path d="M6 42 42 6M16 6h26v26"/></svg>
        </div>
      </nav>
    </div>
  </div>
  <p class="state-note">Full mode in three differnt colors</p>
</section>

<div class="divider" style="top:818px"></div>

<section class="state state--hidden">
  <div class="app-screen">
    <div class="placeholder-photo placeholder-photo--sky" role="img" aria-label="App content photo: stone statue against a blue sky"></div>
    <div class="content-card"><span class="content-card__title">Platzhalter</span></div>
    <div class="placeholder-photo placeholder-photo--sea" role="img" aria-label="App content photo: tropical fish leaping from a water bowl"></div>
    <div class="layer-clip">
      <nav class="promo-tab">
        <div class="promo-tab__tiles">
          <div class="promo-tile"><svg class="icon--ticket" width="44" height="128" viewBox="0 0 44 128"><path d="M8 3h28a5 5 0 0 1 5 5v117l-19-18-19 18V8a5 5 0 0 1 5-5z"/><circle cx="22" cy="32" r="8"/></svg></div>
          <div class="promo-tile"><svg class="icon--like" width="120" height="120" viewBox="0 0 80 80"><path d="M26 34 38 10c4-5 11-2 10 5l-3 14h21c6 0 9 5 7 10l-6 27c-1 4-4 7-8 7H26z"/><path d="M8 34h18v40H8z"/></svg></div>
          <div class="promo-tile"><svg class="icon--device" width="80" height="130" viewBox="0 0 48 80"><rect x="4" y="3" width="40" height="74" rx="6"/><path d="M4 14h40M4 64h40"/><circle cx="24" cy="71" r="1.5"/></svg></div>
        </div>
        <div class="promo-tab__label">
          <span class="promo-tab__text">NEUE ANGEBOTE</span>
          <svg class="promo-tab__arrow" viewBox="0 0 48 48"><path d="M6 42 42 6M16 6h26v26"/></svg>
        </div>
      </nav>
    </div>
  </div>
  <p class="state-note">Hide mode</p>
</section>

<div class="divider" style="top:1642px"></div>

<section class="state state--idle">
  <div class="app-screen">
    <div class="placeholder-photo placeholder-photo--sky" role="img" aria-label="App content photo: stone statue against a blue sky"></div>
    <div class="content-card"><span class="content-card__title">Platzhalter</span></div>
    <div class="placeholder-photo placeholder-photo--sea" role="img" aria-label="App content photo: tropical fish leaping from a water bowl"></div>
    <div class="layer-clip">
      <nav class="promo-tab">
        <div class="promo-tab__tiles">
          <div class="promo-tile"><svg class="icon--ticket" width="44" height="128" viewBox="0 0 44 128"><path d="M8 3h28a5 5 0 0 1 5 5v117l-19-18-19 18V8a5 5 0 0 1 5-5z"/><circle cx="22" cy="32" r="8"/></svg></div>
          <div class="promo-tile"><svg width="120" height="120" viewBox="0 0 80 80"><path d="M26 34 38 10c4-5 11-2 10 5l-3 14h21c6 0 9 5 7 10l-6 27c-1 4-4 7-8 7H26z"/><path d="M8 34h18v40H8z"/></svg></div>
          <div class="promo-tile promo-tile--alt"><svg width="80" height="130" viewBox="0 0 48 80"><rect x="4" y="3" width="40" height="74" rx="6"/><path d="M4 14h40M4 64h40"/><circle cx="24" cy="71" r="1.5"/></svg></div>
        </div>
        <div class="promo-tab__label">
          <span class="promo-tab__text">NEUE ANGEBOTE</span>
          <svg class="promo-tab__arrow" viewBox="0 0 48 48"><path d="M6 42 42 6M16 6h26v26"/></svg>
        </div>
      </nav>
    </div>
  </div>
  <p class="state-note">If there is any new offerings<br>available, the navigation element<br>will be in color els it will in gray</p>
</section>

</body>
</html>
```